Lucid Haven - Need Stationary Design

We need a stationary pack for our new Care company based in the uk
Are corporate colours are Pink and purple
Please use attached logo
Target Market(s)
The Care Industry
Industry/Entity Type
It Company
Contact Information for Business Card
Moira Blythe
Director

```html
<!DOCTYPE html>
<html lang="en">
<head>
<meta charset="utf-8">
<title>Lucid Haven – Stationery</title>
<link href="https://fonts.googleapis.com/css2?family=Questrial&display=swap" rel="stylesheet">
<style>
  :root {
    --bg: #d3d2d5;
    --paper: #f5f5f5;
    --purple: #845fb5;
    --purple-dark: #7a55aa;
    --pink: #d43bb0;
    --ink: #555;
    --motif-light: rgba(200,200,200,0.35);
    --motif-folder: rgba(255,255,255,0.08);
  }
  * { margin: 0; padding: 0; box-sizing: border-box; }
  html, body { width: 1200px; height: 991px; overflow: hidden; }
  body {
    background: var(--bg);
    font-family: "Questrial", sans-serif;
    position: relative;
  }
  .piece { position: absolute; overflow: hidden; }
  .paper { background: var(--paper); }
  .purple { background: var(--purple); }

  .brand { position: absolute; display: flex; flex-direction: column; align-items: center; gap: 6px; }
  .brand-dot { border-radius: 50%; background: var(--pink); }
  .brand-name { white-space: nowrap; color: var(--purple); }
  .on-purple .brand-dot { background: #fff; }
  .on-purple .brand-name { color: #fff; }

  .small-text { position: absolute; color: var(--ink); white-space: nowrap; line-height: 1.45; }
  .small-text .accent { color: var(--pink); }
  .small-text .link { color: var(--purple); }

  .motif { position: absolute; }

  /* letterhead */
  .letterhead { left: 71px; top: 104px; width: 397px; height: 560px; }
  .letterhead .brand { left: 30px; top: 30px; }
  .letterhead .brand-dot { width: 30px; height: 30px; }
  .letterhead .brand-name { font-size: 17px; }
  .letterhead .motif { left: 180px; top: 250px; width: 217px; height: 310px;
    background: radial-gradient(ellipse at 60% 60%, var(--motif-light), transparent 70%); }
  .letterhead .small-text { left: 26px; top: 531px; font-size: 5.5px; }

  /* folder */
  .folder { left: 507px; top: 90px; width: 433px; height: 575px; border-radius: 3px; }
  .folder .spine { position: absolute; left: 26px; top: 0; width: 1px; height: 100%; background: var(--purple-dark); }
  .folder .brand { left: 50%; transform: translateX(-50%); top: 78px; gap: 10px; }
  .folder .brand-dot { width: 54px; height: 54px; }
  .folder .brand-name { font-size: 22px; }
  .folder .motif { left: 50px; top: 230px; width: 340px; height: 345px;
    background: radial-gradient(ellipse at 50% 55%, var(--motif-folder), transparent 70%); }

  /* business cards */
  .card { left: 66px; width: 171px; height: 94px; }
  .card-front { top: 696px; }
  .card-front .brand { left: 12px; top: 12px; gap: 4px; }
  .card-front .brand-dot { width: 18px; height: 18px; }
  .card-front .brand-name { font-size: 9px; }
  .card-front .motif { left: 110px; top: 6px; width: 61px; height: 88px;
    background: linear-gradient(160deg, #a47fd6 0%, #d45ac0 60%, #8a5bb8 100%); opacity: .85; }
  .card-front .small-text { left: 10px; top: 60px; font-size: 3.6px; }
  .card-front .person { font-size: 3.8px; color: #333; margin-bottom: 2px; }
  .card-back { top: 810px; }
  .card-back .brand { left: 18px; top: 20px; gap: 6px; }
  .card-back .brand-dot { width: 24px; height: 24px; }
  .card-back .brand-name { font-size: 10px; }
  .card-back .motif { left: 95px; top: 0; width: 76px; height: 94px;
    background: radial-gradient(ellipse at 50% 60%, var(--motif-folder), transparent 70%); }

  /* DL envelope front */
  .envelope-front { left: 266px; top: 696px; width: 415px; height: 208px; }
  .envelope-front .brand { left: 20px; top: 16px; }
  .envelope-front .brand-dot { width: 34px; height: 34px; }
  .envelope-front .brand-name { font-size: 14px; }
  .envelope-front .small-text { left: 37px; top: 93px; font-size: 4.8px; }
  .envelope-front .motif { left: 282px; top: 16px; width: 133px; height: 192px;
    background: linear-gradient(160deg, #b18ee0 0%, #d862c4 45%, #c22fa8 75%, #7c55b3 100%); opacity: .9; }

  /* envelope back */
  .envelope-back { left: 718px; top: 696px; width: 415px; height: 208px; }
  .envelope-back .flap { position: absolute; left: 0; top: 0; width: 415px; height: 59px; }
  .envelope-back .brand { left: 50%; transform: translateX(-50%); top: 20px; }
  .envelope-back .brand-dot { width: 20px; height: 20px; }
  .envelope-back .small-text { left: 0; width: 100%; text-align: center; top: 180px; font-size: 5px; }
</style>
</head>
<body>

  <section class="piece paper letterhead">
    <div class="brand">
      <span class="brand-dot"></span>
      <span class="brand-name">Lucid Haven</span>
    </div>
    <div class="motif" role="img" aria-label="Faint large brand motif watermark"></div>
    <p class="small-text">
      12 Mere Lane, Alder Court, Hartwell, HW3 2PL<br>
      <span class="accent">T:</span> +44 020 7946 0123 · <span class="accent">E:</span> info@lucidhaven.co.uk · <span class="link">www.lucidhaven.co.uk</span>
    </p>
  </section>

  <section class="piece purple folder on-purple">
    <span class="spine"></span>
    <div class="brand">
      <span class="brand-dot"></span>
      <span class="brand-name">Lucid Haven</span>
    </div>
    <div class="motif" role="img" aria-label="Faint large brand motif on folder cover"></div>
  </section>

  <section class="piece paper card card-front">
    <div class="brand">
      <span class="brand-dot"></span>
      <span class="brand-name">Lucid Haven</span>
    </div>
    <div class="motif" role="img" aria-label="Pink and purple brand motif illustration"></div>
    <div class="small-text">
      <p class="person">MOIRA BLYTHE <span class="accent">| DIRECTOR</span></p>
      12 Mere Lane, Alder Court, Hartwell, HW3 2PL<br>
      <span class="accent">T:</span> +44 020 7946 0123 · <span class="accent">E:</span> info@lucidhaven.co.uk<br>
      <span class="link">www.lucidhaven.co.uk</span>
    </div>
  </section>

  <section class="piece purple card card-back on-purple">
    <div class="motif" role="img" aria-label="Faint brand motif on card back"></div>
    <div class="brand">
      <span class="brand-dot"></span>
      <span class="brand-name">Lucid Haven</span>
    </div>
  </section>

  <section class="piece paper envelope-front">
    <div class="brand">
      <span class="brand-dot"></span>
      <span class="brand-name">Lucid Haven</span>
    </div>
    <p class="small-text">12 Mere Lane, Alder Court<br>Hartwell, HW3 2PL</p>
    <div class="motif" role="img" aria-label="Pink and purple brand motif illustration"></div>
  </section>

  <section class="piece paper envelope-back">
    <svg class="flap" viewBox="0 0 415 59" aria-hidden="true">
      <path d="M0 0 H415 L401 52 Q399 59 392 59 H23 Q16 59 14 52 Z" fill="var(--purple)"/>
    </svg>
    <div class="brand on-purple">
      <span class="brand-dot"></span>
    </div>
    <p class="small-text">www.lucidhaven.co.uk</p>
  </section>

</body>
</html>
```